Marketing One-Sheet for Security Deposit Claim Notice

I need a one-sheet flyer formatted for email distribution — optimized as a JPEG/PNG that I can insert into Constant Contact or Outlook. I do not want to attach it to an email, but insert it in the email we send out. I would like it to look professional but engaging. Some images would be good, but want to make sure it reads well if images do not load for the recipients. The text is in the attached Word document, but I am open to changes/ideas that may be better for marketing purposes. I included the URLs for some of the links I would like in the one-sheet that is clickable. The logo for the business is being uploaded on the Word document. Proposed text is also uploaded in a Word document. Thank you.

Target Market(s)

Landlords, Real Estate Agents, Property Managers

Industry/Entity Type

Legal

Requirements
Must have
• Professional but appealing design. The One-sheet is going to be placed in the body of emails, not as an attachment.
Nice to have
• Include our logo for the business and the web links please.
Should not have
• Images can be ok, but it needs to look right if images do not download from the email sent out.

```html
<!DOCTYPE html>
<html lang="en">
<head>
<meta charset="utf-8">
<title>Security Deposit Claim Notice – Florida Landlords</title>
<link rel="stylesheet" href="https://fonts.googleapis.com/css2?family=Bebas+Neue&family=Lato:ital,wght@0,400;0,700;1,400&family=Playfair+Display:wght@400;700&display=swap">
<style>
:root{
  --red:#a30d1c;
  --red-bright:#e0242f;
  --dark:#2b2b2d;
  --ink:#1f1f1f;
  --grey-panel:#ececec;
  --pink-panel:#fbeaea;
  --white:#ffffff;
  --page-bg:#8f8f8f;
}
*{margin:0;padding:0;box-sizing:border-box}
html,body{width:1200px;height:1137px;overflow:hidden;background:var(--page-bg)}
.flyer{
  position:absolute;left:244px;top:88px;width:650px;height:840px;
  background:var(--white);transform:scale(1.1662);transform-origin:0 0;
  font-family:'Lato',sans-serif;color:var(--ink);overflow:hidden;
}
.abs{position:absolute}
.header-art{position:absolute;left:0;top:0}
.brand{left:30px;top:16px;width:150px;text-align:left}
.brand-name{display:flex;align-items:center;gap:6px;font-family:'Lato',sans-serif;font-weight:700;color:var(--red);font-size:16px;line-height:1.05}
.brand-square{width:12px;height:12px;background:var(--red);flex:none}
.brand-contact{margin-top:6px;font-size:8.5px;font-weight:700;color:var(--red);line-height:1.3}
.title{left:18px;top:118px;font-family:'Bebas Neue',sans-serif;font-weight:400;color:var(--white);font-size:41px;line-height:42px;letter-spacing:.2px}
.audience{left:0;top:213px;width:215px;height:28px;background:var(--dark);color:var(--white);font-family:'Playfair Display',serif;font-weight:400;font-size:15.5px;letter-spacing:.8px;padding-left:18px;line-height:28px}
.tagline{left:16px;top:250px;color:var(--white);font-style:italic;font-size:15px;line-height:20px}
.problem{right:10px;top:226px;width:330px;text-align:right;color:var(--white)}
.problem h2{font-weight:400;color:var(--red-bright);font-size:17px;line-height:20px}
.problem p{font-size:11.3px;line-height:14.5px;margin-top:2px}
.uses-heading{left:0;top:316px;width:650px;text-align:center;font-family:'Playfair Display',serif;font-weight:700;font-size:14px}
.use-box{top:346px;height:40px;background:var(--grey-panel);display:flex;align-items:center;gap:14px;padding-left:8px;font-size:11.5px;line-height:14px}
.panel-head{height:31px;background:var(--red);color:var(--white);text-align:center;font-size:16px;line-height:31px;letter-spacing:.2px}
.risk{left:16px;top:396px;width:301px;height:168px;background:var(--pink-panel)}
.risk .panel-head{margin:6px 0 0 7px;width:294px}
.risk h3{font-family:'Playfair Display',serif;font-size:14.5px;margin:9px 0 0 18px}
.bullets{list-style:none;margin:11px 0 0 18px;font-size:10.8px;line-height:14px}
.bullets li::before{content:"";display:inline-block;border-left:5px solid var(--red);border-top:3.5px solid transparent;border-bottom:3.5px solid transparent;margin-right:4px}
.risk hr{border:0;border-top:1px solid var(--red);margin:6px 18px 0 18px}
.risk .note{font-size:10.8px;margin:7px 0 0 18px}
.diy{left:329px;top:396px;width:308px;height:172px;background:var(--grey-panel)}
.diy .panel-head{margin:6px 0 0 7px;width:294px}
.diy p{text-align:center;font-size:11px;line-height:14px;padding:16px 30px 0}
.diy-cta{left:329px;top:531px;width:308px;height:35px;background:var(--dark);color:var(--white);font-family:'Playfair Display',serif;font-weight:700;font-size:14px;text-align:center;line-height:35px}
.solution{left:23px;top:583px;width:294px}
.solution h4{font-family:'Playfair Display',serif;font-size:11px;text-align:center;margin-top:8px}
.features{list-style:none;margin:8px 0 0 14px;font-size:11.5px}
.features li{display:flex;align-items:center;gap:10px;height:25px}
.divider{left:327px;top:583px;width:2px;height:127px;background:var(--red)}
.pricing{left:336px;top:583px;width:294px}
.price-row{position:absolute;left:337px;height:21px;display:flex;align-items:center;font-size:11.5px}
.price-label{width:60px;height:21px;background:var(--dark);color:var(--white);text-align:center;line-height:21px}
.price-amount{width:76px;height:21px;background:var(--red);color:var(--white);font-weight:700;font-size:14px;line-height:21px;padding-left:16px;clip-path:polygon(0 0,100% 0,88% 100%,0 100%)}
.price-type{margin-left:6px;width:126px}
.price-note{left:338px;top:692px;font-size:11.5px;white-space:nowrap}
.cta{left:14px;top:727px;width:621px;height:34px;display:flex;font-family:'Playfair Display',serif;font-weight:700;font-size:13px}
.cta-primary{width:256px;background:var(--red);color:var(--white);line-height:34px;text-align:center}
.cta-secondary{flex:1;border:1px solid var(--red);line-height:32px;text-align:center;color:var(--ink)}
.footer-art{position:absolute;left:0;top:775px}
.footer-contact{left:12px;top:787px;color:var(--white);font-size:10.5px;line-height:16px;white-space:nowrap}
.footer-contact span{display:flex;align-items:center;gap:4px}
.footer-links{left:242px;top:794px;font-size:10.8px;line-height:16px;color:var(--white);white-space:nowrap}
.footer-links b{color:var(--red-bright);font-weight:700}
.footer-links i{font-style:italic}
</style>
</head>
<body>
<main class="flyer">
  <svg class="header-art" width="650" height="304" viewBox="0 0 650 304">
    <defs>
      <linearGradient id="photoTone" x1="0" y1="0" x2="1" y2="1">
        <stop offset="0" stop-color="#d9d9d9"/>
        <stop offset=".5" stop-color="#8a8a8a"/>
        <stop offset="1" stop-color="#3c3c3c"/>
      </linearGradient>
    </defs>
    <g role="img" aria-label="Black and white photo of a landlord and attorney shaking hands over a desk with a gavel and law books">
      <polygon points="282,0 650,0 650,304 240,304 337,130" fill="url(#photoTone)"/>
    </g>
    <polygon points="287,220 650,220 650,304 240,304" fill="var(--dark)"/>
    <polygon points="270,0 282,0 337,130 240,304 228,304 325,130" fill="#d6d6d6"/>
    <polygon points="0,103 160,103 256,0 270,0 325,130 228,304 0,304" fill="var(--red)"/>
  </svg>

  <div class="abs brand">
    <div class="brand-name"><span class="brand-square"></span>Keystone<br>Landlord Law</div>
    <div class="brand-contact">KeystoneLandlordLaw.com<br>1-800-555-0142</div>
  </div>

  <h1 class="abs title">Security Deposit<br>Claim Notice</h1>
  <div class="abs audience">FLORIDA LANDLORDS</div>
  <p class="abs tagline">Protect Your Right to Keep<br>the Tenant’s Security Deposit</p>

  <section class="abs problem">
    <h2>PROBLEM STATEMENT</h2>
    <p>If a Security Deposit Claim Notice is not prepared correctly or served on time, Florida law automatically favors the tenant — even if rent is unpaid or the property is damaged.</p>
  </section>

  <h2 class="abs uses-heading">When Done Properly, a Security Deposit May Be Used To:</h2>
  <div class="abs use-box" style="left:16px;width:204px"><svg width="26" height="26" viewBox="0 0 26 26"><rect x="2" y="6" width="17" height="17" fill="none" stroke="var(--red)" stroke-width="2"/><path d="M6 14l5 5 12-16" fill="none" stroke="var(--red)" stroke-width="3.5"/></svg><span>Cover Unpaid Rent</span></div>
  <div class="abs use-box" style="left:225px;width:203px"><svg width="26" height="26" viewBox="0 0 26 26"><rect x="2" y="6" width="17" height="17" fill="none" stroke="var(--red)" stroke-width="2"/><path d="M6 14l5 5 12-16" fill="none" stroke="var(--red)" stroke-width="3.5"/></svg><span>Charge against<br>Property Damage</span></div>
  <div class="abs use-box" style="left:436px;width:202px"><svg width="26" height="26" viewBox="0 0 26 26"><rect x="2" y="6" width="17" height="17" fill="none" stroke="var(--red)" stroke-width="2"/><path d="M6 14l5 5 12-16" fill="none" stroke="var(--red)" stroke-width="3.5"/></svg><span>Apply toward Legal<br>Fees and Costs</span></div>

  <section class="abs risk">
    <div class="panel-head">HIGH RISK WARNING</div>
    <h3>If the Claim Notice Is Incorrect or Late:</h3>
    <ul class="bullets">
      <li>Tenant is entitled to a FULL refund of the deposit</li>
      <li>No claim can be made against the deposit</li>
      <li>Tenant can sue the landlord</li>
      <li>Landlord may owe thousands in tenant legal fees</li>
    </ul>
    <hr>
    <p class="note">Even if the tenant owes rent or caused damage.</p>
  </section>

  <section class="abs diy">
    <div class="panel-head">WHY DIY IS DANGEROUS</div>
    <p>There are attorneys who specialize in representing tenants against landlords for improper security deposit claims.<br>They sue, win, and recover substantial legal fees — paid by the landlord.</p>
  </section>
  <div class="abs diy-cta">Avoid Costly Mistakes — Hire Our Firm</div>

  <section class="abs solution">
    <div class="panel-head">YOUR SOLUTION</div>
    <h4>We Prepare &amp; Serve Security Deposit Claim Notices</h4>
    <ul class="features">
      <li><svg width="20" height="20" viewBox="0 0 20 20" fill="none" stroke="var(--red)" stroke-width="1.4"><path d="M10 2v15M4 5h12M4 5l-3 6h6zM16 5l-3 6h6zM6 18h8"/></svg>Complies with Florida statutory requirements</li>
      <li><svg width="20" height="20" viewBox="0 0 20 20" fill="none" stroke="var(--red)" stroke-width="1.6"><circle cx="12" cy="11" r="6.5"/><path d="M12 7v4l2 2M10 3h4M1 9h4M2 12h3M1 15h4"/></svg>Served on time and properly</li>
      <li><svg width="20" height="20" viewBox="0 0 20 20" fill="none" stroke="var(--red)" stroke-width="1.4"><path d="M4 1h8l4 4v9M4 1v17h8M7 7h6M7 10h6M7 13h3"/><circle cx="15" cy="16" r="3"/></svg>Includes required legal wording</li>
    </ul>
  </section>

  <div class="abs divider"></div>

  <section class="abs pricing"><div class="panel-head">PRICING</div></section>
  <div class="price-row" style="top:631px"><span class="price-label">Flat Fee:</span><span class="price-amount">$350</span><span class="price-type">Residential Properties</span><svg width="22" height="20" viewBox="0 0 22 20"><path d="M11 1L1 9h3v10h14V9h3z" fill="var(--red-bright)"/><rect x="9" y="12" width="4" height="7" fill="#fff"/></svg></div>
  <div class="price-row" style="top:659px"><span class="price-label">Flat Fee:</span><span class="price-amount">$450</span><span class="price-type">Commercial Properties</span><svg width="22" height="22" viewBox="0 0 22 22"><rect x="2" y="1" width="18" height="21" fill="var(--red-bright)"/><g fill="#fff"><rect x="5" y="4" width="3" height="3"/><rect x="10" y="4" width="3" height="3"/><rect x="15" y="4" width="2" height="3"/><rect x="5" y="10" width="3" height="3"/><rect x="10" y="10" width="3" height="3"/><rect x="15" y="10" width="2" height="3"/><rect x="9" y="16" width="4" height="6"/></g></svg></div>
  <p class="abs price-note">No hourly billing. No surprises.</p>

  <div class="abs cta">
    <div class="cta-primary">Protect Your Security Deposit Today</div>
    <div class="cta-secondary">Hire Us to Prepare Your Security Deposit Claim Notice</div>
  </div>

  <svg class="footer-art" width="650" height="65" viewBox="0 0 650 65">
    <polygon points="0,2 158,2 194,65 0,65" fill="var(--red)"/>
    <polygon points="246,2 650,2 650,65 199,65" fill="var(--dark)"/>
  </svg>
  <div class="abs footer-contact">
    <span>Keystone Landlord Law</span>
    <span><svg width="9" height="9" viewBox="0 0 10 10" fill="none" stroke="#fff" stroke-width="1"><circle cx="5" cy="5" r="4"/><path d="M1 5h8M5 1c-2 2-2 6 0 8M5 1c2 2 2 6 0 8"/></svg>KeystoneLandlordLaw.com</span>
    <span><svg width="9" height="9" viewBox="0 0 10 10"><path d="M2 1l2 2-1 1.5c.8 1.4 1.6 2.2 3 3L7.5 6l2 2-1.5 1.5C4.5 9 1 5.5.5 2z" fill="#fff"/></svg>1-800-555-0142</span>
  </div>
  <div class="abs footer-links">
    <div><b>More information</b> – [<i>https://keystonelandlordlaw.com/deposit-claims/</i>]</div>
    <div><b>Request our hiring documents</b> - [<i>https://keystonelandlordlaw.com/retain-us/</i>]</div>
  </div>
</main>
</body>
</html>
```